Our Joint Journey - Orthopedic needs from one site

We need slides that help to educate users, interest investors and allow the complexity of the entire continuum of care to be explained so anyone can understand. Our Joint Journey is a Varnolo Health Company. Ourjointjourneyhub.com. We allow people to evaluate, educate and engage with providers from one site. Simplyfying orthopedic care and wellness from one site. Patients, doctors, personal trainers, therapist, nutritionist, yoga, gyms, athletic trainers and more can connect from one site

Target Market(s)

Investors, Patients, Doctors and wellness providers

Industry/Entity Type

Healthcare

Requirements
Must have
• Investor slides, sales slides, education, process....

```html
<!DOCTYPE html>
<html lang="en">
<head>
<meta charset="utf-8">
<title>Our Joint Journey – Slide Deck</title>
<link href="https://fonts.googleapis.com/css2?family=Archivo:wght@400;500;700;800&family=Inter:wght@400;500;700&display=swap" rel="stylesheet">
<style>
:root{
  --stage:#a6a6a6;
  --paper:#ffffff;
  --green:#83c44e;
  --ink:#111111;
  --brand:#1c6ea4;
  --photo-wood:#c9b8a0;
  --photo-blue:#0d3fa8;
}
*{margin:0;padding:0;box-sizing:border-box}
html,body{width:1200px;height:1200px;overflow:hidden;background:var(--stage)}
body{position:relative;font-family:"Inter",sans-serif;color:var(--ink)}
.slide{position:absolute;width:553px;height:415px;background:var(--paper);overflow:hidden;transform:scale(0.621);transform-origin:0 0}
.slide.short{height:403px}
.abs{position:absolute}
.green{position:absolute;background:var(--green)}
.photo{position:absolute}
.running-head{position:absolute;top:30px;left:31px;font-family:"Archivo",sans-serif;font-size:7px;letter-spacing:1.2px;font-weight:500}
.page-no{position:absolute;top:30px;right:31px;font-family:"Archivo",sans-serif;font-size:7px;letter-spacing:1.2px;font-weight:500}
.heading{position:absolute;font-family:"Archivo",sans-serif;font-weight:800;font-size:25px;letter-spacing:2px;line-height:35px;text-transform:uppercase}
.body-copy{position:absolute;font-size:7.6px;line-height:11.8px}
.brand-mark{position:absolute;display:flex;align-items:center;gap:4px;font-family:"Archivo",sans-serif;font-weight:700;font-size:12px;color:var(--brand);line-height:1}
.brand-mark .dot{width:9px;height:9px;border-radius:50%;background:var(--brand)}
.title-lockup{position:absolute;left:330px;top:138px;font-family:"Archivo",sans-serif;font-weight:700;font-size:24px;line-height:29px;letter-spacing:1px;color:var(--brand)}
.issue-list{position:absolute;left:245px;top:226px;font-size:13.5px;line-height:20px;list-style:none}
.issue-list li{padding-left:13px;position:relative}
.issue-list li::before{content:"";position:absolute;left:2px;top:8px;width:4px;height:4px;border-radius:50%;background:var(--ink)}
.service-label{position:absolute;width:112px;text-align:center;font-family:"Archivo",sans-serif;font-weight:800;font-size:18px;letter-spacing:1.5px;top:231px}
.service-copy{position:absolute;top:266px;font-size:7.4px;line-height:11.8px;text-align:justify}
.contact-row{position:absolute;left:260px;font-size:7.2px;display:flex}
.contact-row b{width:80px;font-weight:700}
</style>
</head>
<body>

<!-- Cover -->
<section class="slide" style="left:243.4px;top:119.9px">
  <div class="green" style="left:0;top:0;width:156px;height:415px"></div>
  <div class="photo" role="img" aria-label="Wooden artist's mannequin standing in soft window light" style="left:78px;top:82px;width:168px;height:275px;background:linear-gradient(135deg,#8f8c88,#d8d6d2 55%,var(--photo-wood))"></div>
  <div class="title-lockup">OUR<br>JOINT<br>JOURNEY</div>
  <div class="brand-mark" style="left:455px;top:370px"><span class="dot"></span>Varnolo Health</div>
</section>

<!-- Introduction -->
<section class="slide short" style="left:609.8px;top:127.3px">
  <div class="running-head">OURJOINTJOURNEY</div>
  <div class="page-no">PAGE 01</div>
  <div class="green" style="left:31px;top:128px;width:329px;height:192px"></div>
  <div class="photo" role="img" aria-label="Acupuncture model head with meridian lines" style="left:360px;top:88px;width:193px;height:272px;background:linear-gradient(160deg,#e9ecef,#f7f7f7 60%,#dfe3e6)"></div>
  <h2 class="heading" style="left:41px;top:158px">Introduction</h2>
  <p class="body-copy" style="left:41px;top:196px;width:292px">Our Joint Journey is a Varnolo Health Company. We allow people to evaluate, educate and engage with providers from one site. Simplifying orthopedic care and wellness from one site. Patients, doctors, personal trainers, therapist, nutritionist, yoga, gyms, athletic trainers and more can connect from one site. The site allows patients with a complaint to answer questions and then get a list of likely conditions. They then can educate themselves on these conditions and if they want to find a provider they can find a doctor, therapist, personal trainer and more to help with their wellness journey. From conservative to aggressive and beyond.</p>
</section>

<!-- What is orthopedic -->
<section class="slide" style="left:243.4px;top:385px">
  <div class="running-head">OURJOINTJOURNEY</div>
  <div class="page-no">PAGE 02</div>
  <div class="green" style="left:289px;top:261px;width:264px;height:154px"></div>
  <div class="photo" role="img" aria-label="Blue anatomical illustration of a running figure with a highlighted knee" style="left:330px;top:113px;width:169px;height:187px;background:radial-gradient(circle at 50% 45%,#2fb8ee,var(--photo-blue) 60%,#06126b)"></div>
  <div class="abs" style="left:465px;top:326px;width:88px;height:89px;background:var(--paper)"></div>
  <h2 class="heading" style="left:31px;top:112px">What is<br>orthopedic</h2>
  <p class="body-copy" style="left:22px;top:220px;width:245px">Orthopedic surgery or orthopedics, is the branch of surgery concerned with conditions involving the musculoskeletal system. Orthopedic surgeons use both surgical and nonsurgical means to treat musculoskeletal trauma, spine diseases, sports injuries, degenerative diseases, infections, tumors, and congenital disorders.</p>
  <div class="brand-mark" style="left:470px;top:366px;font-size:10px"><span class="dot"></span>Varnolo</div>
</section>

<!-- What we do -->
<section class="slide" style="left:609.8px;top:385px">
  <div class="running-head">OURJOINTJOURNEY</div>
  <div class="page-no">PAGE 04</div>
  <div class="green" style="left:341px;top:0;width:212px;height:170px"></div>
  <div class="green" style="left:0;top:281px;width:252px;height:134px"></div>
  <div class="photo" role="img" aria-label="Clinician in teal scrubs holding a stethoscope" style="left:368px;top:92px;width:168px;height:228px;background:linear-gradient(160deg,#eef0ef,#8fd3c2 55%,#e9e6e2)"></div>
  <div class="photo" role="img" aria-label="People training on treadmills in a gym" style="left:34px;top:234px;width:114px;height:94px;background:linear-gradient(135deg,#9aa6b3,#4a5664)"></div>
  <div class="photo" role="img" aria-label="Stack of books with letter blocks spelling study" style="left:173px;top:234px;width:115px;height:94px;background:linear-gradient(160deg,#3b4a44,#c7703e 60%,#b5612f)"></div>
  <h2 class="heading" style="left:31px;top:115px">What we do</h2>
  <p class="body-copy" style="left:31px;top:154px;width:292px">We allow patients with a complaint to answer questions and then get a list of likely conditions. They then can educate themselves on these conditions and if they want to find a provider they can find a doctor, therapist, personal trainer and more to help with their wellness journey. From conservative to aggressive and beyond.</p>
  <div class="brand-mark" style="left:470px;top:368px;font-size:10px"><span class="dot"></span>Varnolo</div>
</section>

<!-- Orthopedic problems -->
<section class="slide" style="left:243.4px;top:649.6px">
  <div class="green" style="left:0;top:0;width:106px;height:415px"></div>
  <div class="running-head">OURJOINTJOURNEY</div>
  <div class="page-no">PAGE 03</div>
  <div class="photo" role="img" aria-label="Man holding his lower back with pain highlighted" style="left:48px;top:84px;width:116px;height:96px;background:linear-gradient(135deg,#d9d9d9,#9b8f89 60%,#c94b3b)"></div>
  <div class="photo" role="img" aria-label="Man holding his elbow with pain highlighted" style="left:171px;top:41px;width:134px;height:91px;background:linear-gradient(135deg,#e3e3e3,#a7a09c 60%,#d7d7d7)"></div>
  <div class="photo" role="img" aria-label="X-ray style figure holding an inflamed knee" style="left:48px;top:214px;width:175px;height:159px;background:radial-gradient(circle at 55% 30%,#e35a2a,#3c3c3c 30%,#050505)"></div>
  <h2 class="heading" style="left:276px;top:131px">Orthopedic<br>problems</h2>
  <ul class="issue-list">
    <li>Lower Back Pain. Lower back pain is one<br>of the most common orthopedic issues. ...</li>
    <li>Knee pain.</li>
    <li>Hamstring injuries.</li>
    <li>Plantar fasciitis.</li>
    <li>Scoliosis.</li>
    <li>Hip Fracture.</li>
    <li>Arthritis.</li>
  </ul>
  <div class="brand-mark" style="left:472px;top:366px;font-size:10px"><span class="dot"></span>Varnolo</div>
</section>

<!-- Other services -->
<section class="slide" style="left:609.8px;top:649.6px">
  <div class="green" style="left:0;top:0;width:553px;height:211px"></div>
  <div class="running-head">OURJOINTJOURNEY</div>
  <div class="page-no">PAGE 05</div>
  <h2 class="heading" style="left:31px;top:72px">Other services</h2>
  <div class="photo" role="img" aria-label="Person meditating in a yoga pose by candlelight" style="left:51px;top:139px;width:112px;height:91px;background:linear-gradient(135deg,#5a3f2c,#c9a58a 55%,#8a6246)"></div>
  <div class="photo" role="img" aria-label="Athlete lifting a barbell in a gym" style="left:220px;top:139px;width:112px;height:91px;background:linear-gradient(135deg,#1d2b38,#3f6a84 55%,#20262c)"></div>
  <div class="photo" role="img" aria-label="Therapist's notepad and pen on a desk" style="left:390px;top:139px;width:112px;height:91px;background:linear-gradient(135deg,#2a231e,#8a6a4a 55%,#d8d2c8)"></div>
  <div class="service-label" style="left:51px">YOGA</div>
  <div class="service-label" style="left:220px">GYM</div>
  <div class="service-label" style="left:390px">THERAPY</div>
  <p class="service-copy" style="left:31px;width:153px">Yoga is a vast collection of spiritual techniques and practices aimed at integrating mind, body and spirit to achieve a state of enlightenment or oneness with the universe. Though yoga's ultimate aim is lofty, its essence is practical and scientific as it emphasizes direct experience and observable results</p>
  <p class="service-copy" style="left:200px;width:153px">Exercise can help prevent excess weight gain or help maintain weight loss. When you engage in physical activity, you burn calories. The more intense the activity, the more calories you burn.</p>
  <p class="service-copy" style="left:385px;width:127px">Therapy is a positive way to deal with trauma, pain, or any issue you have in life so you can become a healthier, happier, more peaceful person. When you develop coping skills, learn how to let go of negativity, set boundaries.</p>
  <div class="brand-mark" style="left:470px;top:372px;font-size:10px"><span class="dot"></span>Varnolo</div>
</section>

<!-- Educate and evaluate -->
<section class="slide" style="left:243.4px;top:916px">
  <div class="green" style="left:361px;top:0;width:192px;height:415px"></div>
  <div class="running-head">OURJOINTJOURNEY</div>
  <div class="page-no">PAGE 06</div>
  <h2 class="heading" style="left:31px;top:98px">Educate and<br>evaluate</h2>
  <div class="photo" role="img" aria-label="Hands holding a tablet showing an evaluation form with red icons" style="left:31px;top:178px;width:344px;height:215px;background:linear-gradient(135deg,#a89a9a,#cfc5c4 55%,#9e3a3a)"></div>
</section>

<!-- Contact -->
<section class="slide" style="left:609.8px;top:916px">
  <div class="running-head">OURJOINTJOURNEY</div>
  <div class="page-no">PAGE 07</div>
  <div class="green" style="left:0;top:106px;width:128px;height:225px"></div>
  <div class="photo" role="img" aria-label="Screenshot of the website's evaluation page" style="left:26px;top:124px;width:213px;height:94px;background:linear-gradient(135deg,#0c2a5a,#3a6ea8 55%,#0f2f5c)"></div>
  <h2 class="heading" style="left:260px;top:156px">Contact</h2>
  <div class="contact-row" style="top:214px"><b>E-mail</b><span>hello@ourjointjourneyhub.com</span></div>
  <div class="contact-row" style="top:233px"><b>Website</b><span>www.Ourjointjourneyhub.com</span></div>
  <div class="contact-row" style="top:252px"><b>Phone</b><span>+123-555-0142</span></div>
  <div class="contact-row" style="top:271px"><b>Address</b><span></span></div>
</section>

</body>
</html>
```